University of Carrowmere Lindell Saxophone Quartet Concert

We need a poster design advertising the Lindell Saxophone Quartet Concert on Tuesday, April 23 at 5pm. The program concert will consist of 2 works by Peter Voskuilen: Harbor Lanterns and Meridian ledger. These two works should be included on the poster being the concert is featuring the composer and his works. Peter Voskuilen is known for his very "natural" sounding music. He resides in Montana and writes mostly from his small cottage in the mountains. This same idea of nature and "Montana" should be included on the poster design. He is deeply influenced by Thrane and most of the music he writes is play offs from Thrane Chorales.

The concert title is: "Where Stillness Gathers Near"

Target Market(s)

Collegiate Musician, Professional Musicians, Music Faculty

Industry/Entity Type

Advertising

Requirements
Must have
• 1. Title of the Concert: "Where Stillness Gathers Near"
2. "Lindell Saxophone Quartet Presents"
3. Date (April 23)
4. Time: 5pm
5. Location: Chapel of The Gentle Osric
Nice to have
• Nice to maybe keep the idea of "Montana" and that mountian-esque feel

```html
<!DOCTYPE html>
<html lang="en">
<head>
<meta charset="utf-8">
<title>Where Stillness Gathers Near — Lindell Saxophone Quartet</title>
<link href="https://fonts.googleapis.com/css2?family=Archivo+Black&family=Bebas+Neue&family=Arimo:wght@400;700&display=swap" rel="stylesheet">
<style>
  :root {
    --page: #ffffff;
    --wood-dark: #141414;
    --wood-mid: #2e2e2e;
    --wood-light: #4a4a4a;
    --ink-light: #ffffff;
    --band: #333132;
    --band-sub: #a9a9a9;
    --sky: #5a6370;
    --hill-green: #6f7a3a;
    --hill-gold: #c9b436;
    --hill-rust: #a8502a;
  }
  * { margin: 0; padding: 0; box-sizing: border-box; }
  html, body { width: 1200px; height: 1000px; overflow: hidden; background: var(--page); }
  .poster {
    position: absolute; left: 20px; top: 20px;
    width: 719px; height: 957px; overflow: hidden;
    background: var(--wood-dark);
  }
  .wood-photo {
    position: absolute; left: 0; top: 0; width: 100%; height: 515px;
    background:
      radial-gradient(ellipse at 55% 35%, var(--wood-light) 0%, transparent 55%),
      linear-gradient(170deg, var(--wood-dark) 0%, var(--wood-mid) 45%, #1c1c1c 100%);
  }
  .ledge {
    position: absolute; left: 0; top: 490px; width: 100%; height: 40px;
    background: linear-gradient(180deg, #0d0d0d, #222);
  }
  .landscape-photo {
    position: absolute; left: 0; top: 525px; width: 100%; height: 432px;
    background:
      linear-gradient(180deg, #2a2d33 0%, var(--sky) 14%, #59624c 28%, var(--hill-green) 42%, var(--hill-rust) 52%, var(--hill-gold) 70%, #9aa048 84%, #a9a07a 100%);
  }
  .title {
    position: absolute; right: 44px; top: 94px;
    font-family: "Archivo Black", "Arial Black", sans-serif;
    font-size: 62px; line-height: 72px; color: var(--ink-light);
    text-align: right;
  }
  .presenter {
    position: absolute; right: 76px; top: 264px;
    font-family: "Arimo", Arial, sans-serif; font-size: 24px; color: var(--ink-light);
  }
  .composer {
    position: absolute; right: 44px; top: 356px;
    font-family: "Arimo", Arial, sans-serif; font-weight: 700;
    font-size: 56px; line-height: 64px; color: var(--ink-light);
  }
  .works {
    position: absolute; right: 44px; top: 418px;
    font-family: "Bebas Neue", "Arial Narrow", sans-serif;
    font-size: 27px; color: var(--ink-light);
  }
  .venue-band {
    position: absolute; left: 0; top: 734px; width: 100%; height: 102px;
    background: var(--band);
  }
  .venue {
    position: absolute; right: 44px; top: 18px;
    font-family: "Bebas Neue", "Arial Narrow", sans-serif;
    font-size: 37px; line-height: 40px; color: var(--ink-light);
  }
  .date-time {
    position: absolute; right: 44px; top: 62px;
    font-family: "Arimo", Arial, sans-serif; font-size: 21px; color: var(--band-sub);
  }
</style>
</head>
<body>
  <main class="poster">
    <div class="wood-photo" role="img" aria-label="Close-up photograph of dark weathered wood grain"></div>
    <div class="ledge"></div>
    <div class="landscape-photo" role="img" aria-label="Photograph of autumn mountain hillside in green, gold and rust tones"></div>

    <h1 class="title">Where Stillness<br>Gathers Near</h1>
    <p class="presenter">Lindell Saxophone Quartet Presents</p>
    <h2 class="composer">Peter Voskuilen</h2>
    <p class="works">Harbor Lanterns &amp; Meridian Ledger</p>

    <section class="venue-band">
      <p class="venue">Chapel of The Gentle Osric</p>
      <p class="date-time">April 23 • 2013 / 5 pm</p>
    </section>
  </main>
</body>
</html>
```